Van/Car Signage

I'm looking for artwork designs for signwriting for our company cars & Vans. 1 x 2023 Velko Stratum Parowen & 1 x 2024 Holm Ravenette LWB Both are White. You can access our company details and product range at www.quillmereprovisionhaus.com.au - i have uploaded our logo.

```html
<!DOCTYPE html>
<html lang="en">
<head>
<meta charset="utf-8">
<title>Quillmere Provision Haus – Vehicle Signage</title>
<link rel="stylesheet" href="https://fonts.googleapis.com/css2?family=Rubik:wght@700&family=Roboto:ital,wght@1,900&display=swap">
<style>
  :root {
    --brand-blue: #2a6fc0;
    --brand-red: #e8232b;
    --ink-white: #ffffff;
    --canvas-bg: #ffffff;
  }
  html, body {
    margin: 0;
    padding: 0;
    overflow: hidden;
    background: var(--canvas-bg);
  }
  .signage {
    position: relative;
    width: 900px;
    height: 1200px;
    overflow: hidden;
    background: var(--canvas-bg);
  }
  .brand-name {
    position: absolute;
    top: 250px;
    left: 0;
    width: 900px;
    display: flex;
    justify-content: center;
    align-items: center;
    gap: 28px;
  }
  .brand-square {
    width: 70px;
    height: 70px;
    background: var(--brand-red);
    flex: none;
  }
  .brand-wordmark {
    font-family: "Rubik", sans-serif;
    font-weight: 700;
    color: var(--brand-blue);
    font-size: 76px;
    line-height: 0.98;
    letter-spacing: -1px;
    margin: 0;
  }
  .contact-list {
    position: absolute;
    top: 520px;
    left: 140px;
    width: 620px;
    margin: 0;
    padding: 0;
    list-style: none;
    display: flex;
    flex-direction: column;
    gap: 20px;
  }
  .contact-row {
    height: 64px;
    margin: 0;
    background: var(--brand-red);
    display: flex;
    align-items: center;
    padding-left: 26px;
    box-sizing: border-box;
    font-family: "Roboto", sans-serif;
    font-style: italic;
    font-weight: 900;
    color: var(--ink-white);
    white-space: nowrap;
  }
  .row-offer { font-size: 31px; letter-spacing: 1px; }
  .row-phone { font-size: 31px; letter-spacing: 9px; }
  .row-email { font-size: 22px; letter-spacing: -0.3px; }
  .row-local { font-size: 22px; }
</style>
</head>
<body>
  <main class="signage">
    <header class="brand-name">
      <span class="brand-square"></span>
      <h1 class="brand-wordmark">Quillmere<br>Provision Haus</h1>
    </header>

    <ul class="contact-list">
      <li class="contact-row row-offer">Free Measure &amp; Quote</li>
      <li class="contact-row row-phone">(03) 9000 4172</li>
      <li class="contact-row row-email">sales@quillmereprovisionhaus.com.au</li>
      <li class="contact-row row-local">Locally made by us! 10 years Exprience</li>
    </ul>
  </main>
</body>
</html>
```